Career development coaching - school lever to adults, needs a business card

Tandem Lark - An independent Career Advice business that provides 1-2-1 advice,for career development, entrepreneurial support and workshops needs a business card. Our clients of all ages (school leaver to adults looking for a career move) and universities and colleges. We would like the card to be double-sided with a modern, professional look. Looking for something professional yet very creative and original. Want a standard size business card that inspires a second look because it stands out from the rest.

One side of the card to have a design incorporating the logo with Tandem Lark name with the strap line “Helping you find your future” and space for the company website

Other side of the card to the logo/Tandem Lark name and the usual contact information:
Individual Name
Job Title (for example, Director)
Phone number
Email address
Company website address

Facebook, LinkedIn and Twitter links will need to go somewhere (back or front!)

The design will be used for 3 individuals so should be editable so that we can update as needed/as we grow.

Attached is the company logo/colours to be incorporated.

Target Market(s)

1-2-1 advice,for career development, entrepreneurial support and workshops needs a business card. Our clients of all ages (school leaver to adults looking for a career move) and universities and colleges.

Industry/Entity Type

Consulting

Contact Information for Business Card

Individual Name
Phone number
Email address
Company website address

Font styles to use
Sans Serif

Colors
0255a3
3176b5
faa54b
f78f20
85acd3
cfdeed

Requirements
Must have
• use the Tandem Lark Logo in some way - using the colours and the blue/orange palette
• For the logo - hope this makes sense to someone or if they direclty relate to the logo image attached!
• For the Orange:- Pantone 1585 C
• In CMYK : C3 M71 Y100 K0
• For the Blue:- 100% Pantone 7469 C
• In CMYK : C100 M62 Y27 K7
• Please feel free to contact me with any questions for more info
Nice to have
• happy to see any creative designs
Should not have
• Nothing too traditional,

```html
<!DOCTYPE html>
<html lang="en">
<head>
<meta charset="utf-8">
<title>Tandem Lark – Business Card</title>
<link rel="stylesheet" href="https://fonts.googleapis.com/css2?family=Hind:wght@300;400;500;600&display=swap">
<style>
  :root {
    --orange: #faa54b;
    --orange-deep: #f78f20;
    --orange-burnt: #e8640c;
    --cream: #fff1e0;
    --blue: #0255a3;
    --ink: #4a3520;
    --paper: #ffffff;
    --backdrop: #e4e4e4;
  }
  * { box-sizing: border-box; margin: 0; padding: 0; }
  html, body {
    width: 1200px; height: 1000px; overflow: hidden;
    background: var(--backdrop);
    font-family: "Hind", Arial, sans-serif;
  }
  .sheet {
    width: 1200px; height: 1000px;
    display: flex; flex-direction: column; align-items: center; justify-content: center;
    gap: 60px;
  }
  .card {
    width: 700px; height: 390px; position: relative; overflow: hidden;
    box-shadow: 0 6px 18px rgba(0,0,0,0.12);
  }

  /* Front */
  .card-front { background: var(--orange); }
  .strapline {
    position: absolute; left: 48px; top: 52px;
    font-weight: 500; font-size: 44px; line-height: 50px; letter-spacing: 1px;
    text-transform: uppercase; color: var(--cream);
  }
  .strapline span { display: block; }
  .front-rule {
    position: absolute; left: 50px; top: 220px;
    width: 80px; height: 4px; background: var(--blue);
  }
  .front-web {
    position: absolute; left: 50px; bottom: 34px;
    font-size: 21px; font-weight: 400; letter-spacing: 1px; color: var(--orange-burnt);
  }
  .front-mark {
    position: absolute; right: 48px; bottom: 30px;
    display: flex; align-items: center; gap: 12px;
  }
  .front-mark .dot { width: 30px; height: 30px; border-radius: 50%; background: var(--blue); }
  .front-mark .name {
    font-size: 22px; font-weight: 600; letter-spacing: 2px; text-transform: uppercase; color: var(--blue);
  }

  /* Back */
  .card-back { display: flex; background: var(--paper); }
  .back-details {
    width: 430px; height: 100%; background: #fba24f;
    padding: 96px 0 0 88px; color: var(--ink);
    font-size: 19px; font-weight: 300; line-height: 26px;
  }
  .person { font-weight: 600; color: var(--blue); font-size: 19px; }
  .role { margin-bottom: 26px; }
  .contact-group { margin-bottom: 22px; }
  .row { display: flex; align-items: center; gap: 7px; }
  .row svg { flex: none; }
  .social-square { width: 12px; height: 12px; background: var(--ink); flex: none; }
  .back-brand {
    flex: 1; display: flex; flex-direction: column; align-items: center; justify-content: center; gap: 16px;
  }
  .back-brand .dot { width: 62px; height: 62px; border-radius: 50%; background: var(--blue); }
  .back-brand .name {
    font-size: 23px; font-weight: 600; letter-spacing: 2px; text-transform: uppercase; color: var(--blue);
  }
</style>
</head>
<body>
<main class="sheet">
  <section class="card card-front" aria-label="Card front">
    <h1 class="strapline"><span>Helping you</span><span>find your future</span></h1>
    <div class="front-rule"></div>
    <p class="front-web">WWW.TANDEMLARK.COM</p>
    <div class="front-mark">
      <div class="dot"></div>
      <div class="name">Tandem Lark</div>
    </div>
  </section>

  <section class="card card-back" aria-label="Card back">
    <div class="back-details">
      <p class="person">Mara L Penn</p>
      <p class="role">Director</p>
      <div class="contact-group">
        <p class="row">
          <svg width="10" height="15" viewBox="0 0 10 15" aria-hidden="true"><rect x="1" y="1" width="8" height="13" rx="1.5" fill="none" stroke="#4a3520" stroke-width="1.4"/><circle cx="5" cy="11.5" r="0.9" fill="#4a3520"/></svg>
          +01 555 010 22
        </p>
        <p class="row">
          <svg width="14" height="11" viewBox="0 0 14 11" aria-hidden="true"><rect x="0.7" y="0.7" width="12.6" height="9.6" fill="#4a3520"/><path d="M1 1 L7 6 L13 1" fill="none" stroke="#fba24f" stroke-width="1.2"/></svg>
          mara@tandemlark.com
        </p>
      </div>
      <p>www.tandemlark.com</p>
      <p class="row"><span class="social-square"></span>Company address</p>
      <p class="row"><span class="social-square"></span>Company address</p>
      <p class="row"><span class="social-square"></span>Company address</p>
    </div>
    <div class="back-brand">
      <div class="dot"></div>
      <div class="name">Tandem Lark</div>
    </div>
  </section>
</main>
</body>
</html>
```